letterhead design using our existing logo

We are a small boutique property management business based in Sydney's Northern Beaches.
We are after a sleek, simple modern letterhead (A4) incorporating our logo and its colours.
Also matching envelope (DL)
I have attached the logo with black text and white text for design options.

Target Market(s)

29-69yo Male and Female

Industry/Entity Type

Property Management

Requirements
Must have
• - Estate Haven logo
• - Address, number and website:
• Suite 7, 18-19 Harlow Parade, Brenton NSW 2187
• Tel: Carl Doyle 0419 267 530 Miriam Kovacs 0407 516 948 www.estatehavenrealty.com.au
Nice to have
• sleek design that looks modern and professional
Should not have
• too many colours or too busy

```html
<!DOCTYPE html>
<html lang="en">
<head>
<meta charset="utf-8">
<title>Estate Haven Stationery</title>
<link href="https://fonts.googleapis.com/css2?family=Roboto:wght@400;700&display=swap" rel="stylesheet">
<style>
  :root {
    --backdrop: #a4a4a4;
    --paper: #ffffff;
    --ink: #111111;
    --muted: #333333;
    --teal-light: #2c9fa3;
    --teal-dark: #157b8b;
    --rule: #2c9fa3;
  }
  * { box-sizing: border-box; margin: 0; padding: 0; }
  html, body { width: 1200px; height: 906px; overflow: hidden; }
  body {
    background: var(--backdrop);
    font-family: "Roboto", Arial, sans-serif;
    color: var(--ink);
    position: relative;
  }
  .sheet {
    position: absolute;
    background: var(--paper);
    box-shadow: 4px 4px 8px rgba(0,0,0,0.35);
    overflow: hidden;
  }
  .letterhead { left: 48px; top: 77px; width: 504px; height: 714px; }
  .envelope { left: 596px; width: 565px; height: 282px; }
  .envelope-front { top: 151px; }
  .envelope-back { top: 465px; }

  .brand-name {
    position: absolute;
    font-weight: 700;
    color: var(--ink);
    white-space: nowrap;
    line-height: 1;
    text-transform: uppercase;
    letter-spacing: -0.2px;
  }
  .letterhead .brand-name { right: 48px; top: 47px; font-size: 20px; }
  .envelope-front .brand-name { left: 20px; top: 35px; font-size: 15px; }
  .envelope-back .brand-name { left: 0; right: 0; text-align: center; top: 39px; font-size: 15px; }

  .brand-band { position: absolute; left: 0; bottom: 0; width: 100%; display: block; }
  .letterhead .brand-band { height: 18px; }
  .envelope-front .brand-band { height: 20px; }

  .return-address {
    position: absolute;
    left: 148px; top: 32px;
    padding-left: 10px;
    border-left: 1px solid var(--rule);
    font-size: 8px;
    line-height: 11px;
    color: var(--muted);
  }

  .contact-footer {
    position: absolute;
    left: 50px; top: 675px;
    display: flex;
    font-size: 6.2px;
    line-height: 9px;
    color: var(--muted);
  }
  .contact-col { padding: 0 6px; border-left: 1px solid var(--muted); }
  .contact-col:first-child { border-left: none; padding-left: 0; }
  .contact-line { display: flex; align-items: center; gap: 3px; white-space: nowrap; }
  .contact-line svg { width: 6px; height: 6px; flex: none; }

  .flap { position: absolute; left: 0; top: 0; width: 565px; height: 100px; }
</style>
</head>
<body>

<section class="sheet letterhead">
  <div class="brand-name">Estate Haven</div>
  <div class="contact-footer">
    <div class="contact-col">
      <div class="contact-line">
        <svg viewBox="0 0 10 10"><path d="M1 4 Q5 0 9 4 L8 5 L6 4 L6 3 L4 3 L4 4 L2 5 Z M2 6 H8 V9 H2 Z" fill="var(--teal-dark)"/></svg>
        0419 267 530 (Carl Doyle)
      </div>
      <div class="contact-line">
        <svg viewBox="0 0 10 10"><path d="M1 4 Q5 0 9 4 L8 5 L6 4 L6 3 L4 3 L4 4 L2 5 Z M2 6 H8 V9 H2 Z" fill="var(--teal-dark)"/></svg>
        0407 516 948 (Miriam Kovacs)
      </div>
    </div>
    <div class="contact-col">
      <div class="contact-line">
        <svg viewBox="0 0 10 10"><rect x="1" y="2" width="8" height="6" fill="var(--teal-dark)"/><path d="M1 2 L5 6 L9 2" stroke="#fff" fill="none" stroke-width="0.8"/></svg>
        info@estatehavenrealty.com.au
      </div>
      <div class="contact-line">
        <svg viewBox="0 0 10 10"><circle cx="5" cy="5" r="4" fill="none" stroke="var(--teal-dark)" stroke-width="1"/><path d="M1 5 H9 M5 1 V9" stroke="var(--teal-dark)" stroke-width="0.8"/></svg>
        www.estatehavenrealty.com.au
      </div>
    </div>
    <div class="contact-col">
      <div>Suite 7, 18-19 Harlow Parade</div>
      <div>Brenton NSW 2187</div>
    </div>
  </div>
  <svg class="brand-band" viewBox="0 0 504 18" preserveAspectRatio="none" aria-hidden="true">
    <polygon points="0,0 361,0 354,18 0,18" fill="var(--teal-light)"/>
    <polygon points="367,0 504,0 504,18 360,18" fill="var(--teal-dark)"/>
  </svg>
</section>

<section class="sheet envelope envelope-front">
  <div class="brand-name">Estate Haven</div>
  <div class="return-address">
    <div>Suite 7, 18-19 Harlow Parade</div>
    <div>Brenton NSW 2187</div>
  </div>
  <svg class="brand-band" viewBox="0 0 565 20" preserveAspectRatio="none" aria-hidden="true">
    <polygon points="0,0 399,0 392,20 0,20" fill="var(--teal-light)"/>
    <polygon points="405,0 565,0 565,20 398,20" fill="var(--teal-dark)"/>
  </svg>
</section>

<section class="sheet envelope envelope-back">
  <svg class="flap" viewBox="0 0 565 100" aria-hidden="true">
    <path d="M1 4 C6 40 10 80 13 86 Q15 90 20 90 L546 89 Q551 89 553 84 C556 76 560 40 563 4" fill="none" stroke="var(--teal-light)" stroke-width="0.9"/>
  </svg>
  <div class="brand-name">Estate Haven</div>
</section>

</body>
</html>
```